Fahrzeugbeschriftung für ein Gebäudereinigungsunternehmen
Zielgruppe
Wir sind ein modernes, regional tätiges Gebäudereinigungsunternehmen, das seit 40 Jahren besteht. Unsere Kunden kommen zu 80% aus Gewerbe und 20% sind Privatkunden. Im regionalen Einzugsgebiet sind wir als Unternehmen bekannt.
Aufgabenstellung
Der Design Entwurf soll für einen MT Borvan sein.
MT Borvan 35 Kasten (Baujahr 2026)
Farbe: Oyster Silver Metallic
Radstand: 3640mm mit Hochdach
Seitenwände und Heckflügeltüren geschlossen
Unsere Firmenfarbe ist rot. Das Firmenlogo rot, grau (Datei & Designbeschreibung im Anhang).
Bisher haben wir die Fahrzeuge klassisch mit Logo und Adressblock foliert.
Aufgabe:
Wir suchen ein modernes, dynamisches Design für die großflächige Folierung (Teilfolierung) unserer Firmenfahrzeuge. Das Design soll Professionalität ausstrahlen, im Straßenverkehr auffallen und unsere Markenidentität perfekt transportieren. Das Firmenlogo soll das zentrale Element sein und aus der Distanz sowie im fließenden Verkehr erkennbar sein.
Design-Vorgaben:
• Logo: Muss prominent und klar erkennbar eingearbeitet werden.
• Farben: Fahrzeugfarbe ist oyster silver metallic. Unsere Firmenfarbe ist Rot. Das Logo ist Rot/Grau (Datei & Designbeschreibung im Anhang). Diese Palette soll sich im Design widerspiegeln.
• Stil: Modern, clean, nicht überladen. Gerne mit großflächigen, dynamischen Elementen (Teilfolierung), die den silbernen Originallack geschickt integrieren.
• Textur/Elemente: Erlaubt sind abstrakte Formen, Linien, geometrische Muster oder großflächige Farbblöcke.
Was wir NICHT wollen (Ausschlusskriterien):
• Keine Gesichter, Fotos oder Stock-Bilder von putzenden Menschen.
• Keine altbackenen Piktogramme (keine Eimer, Schrubber, Leitern oder Blasen).
Wir freuen uns auf eure kreativen und mutigen Ideen!

```html
<!DOCTYPE html>
<html lang="de">
<head>
<meta charset="utf-8">
<title>Brunnhof Gebäudereinigung – Fahrzeugbeschriftung</title>
<link rel="stylesheet" href="https://fonts.googleapis.com/css2?family=Open+Sans:wght@400;700&display=swap">
<style>
  :root {
    --bg: #ffffff;
    --paint: #cdd2d5;
    --paint-edge: #b7bcc0;
    --glass: #e4e7e9;
    --trim: #3a3e41;
    --tyre: #262829;
    --rim: #c3c7ca;
    --brand-red: #a53140;
    --brand-grey: #8b8f92;
    --stripe-text: #d9dcde;
  }
  html, body {
    margin: 0;
    padding: 0;
    width: 1200px;
    height: 900px;
    overflow: hidden;
    background: var(--bg);
  }
  .canvas {
    width: 1200px;
    height: 900px;
    display: block;
  }
  .van-body { fill: var(--paint); stroke: var(--paint-edge); stroke-width: 1.5; }
  .van-glass { fill: var(--glass); stroke: var(--paint-edge); stroke-width: 1.5; }
  .panel-seam { fill: none; stroke: var(--paint-edge); stroke-width: 1.5; }
  .lower-trim { fill: var(--trim); }
  .wheel-arch { fill: var(--trim); }
  .tyre { fill: var(--tyre); }
  .rim { fill: var(--rim); stroke: #9a9ea1; stroke-width: 2; }
  .hub { fill: #8e9295; }
  .shadow { fill: #e9eaeb; }
  .brand-stripe { fill: var(--brand-red); }
  .rear-disc { fill: var(--brand-red); }
  .stripe-url {
    font-family: "Open Sans", sans-serif;
    font-weight: 700;
    font-size: 27px;
    fill: var(--stripe-text);
  }
  .brand-name {
    font-family: "Open Sans", sans-serif;
    font-weight: 700;
    font-size: 36px;
    letter-spacing: 10px;
    fill: var(--brand-red);
  }
  .brand-tagline {
    font-family: "Open Sans", sans-serif;
    font-weight: 400;
    font-size: 11px;
    letter-spacing: 2.2px;
    fill: var(--brand-grey);
  }
</style>
</head>
<body>
<svg class="canvas" viewBox="0 0 1200 900" xmlns="http://www.w3.org/2000/svg">
  <ellipse class="shadow" cx="580" cy="662" rx="520" ry="12"/>

  <g role="img" aria-label="Seitenansicht Kastenwagen mit Hochdach in Silber">
    <path class="van-body" d="M330 268 C380 250 450 244 500 244 L1030 245 C1042 246 1046 252 1047 262 L1052 600 L1078 604 L1076 628 L900 630 L300 630 L190 628 L78 620 L74 560 L88 492 C120 472 170 460 232 440 Z"/>
    <path class="van-glass" d="M370 320 L461 318 L462 437 L308 437 C330 392 350 345 370 320 Z"/>
    <rect class="panel-seam" x="500" y="316" width="522" height="120" rx="8"/>
    <line class="panel-seam" x1="484" y1="250" x2="484" y2="600"/>
    <line class="panel-seam" x1="753" y1="248" x2="753" y2="600"/>
  </g>

  <path class="brand-stripe" d="M150 494 L1048 444 L1048 500 L178 540 Z"/>
  <text class="stripe-url" x="330" y="516" transform="rotate(-3.2 330 516)">WWW.BRUNNHOF-REINIGUNG.DE</text>

  <circle class="rear-disc" cx="947" cy="465" r="56"/>

  <text class="brand-name" x="849" y="380" text-anchor="end">BRUNNHOF</text>
  <text class="brand-tagline" x="849" y="397" text-anchor="end">GEBÄUDEREINIGUNG</text>

  <path class="lower-trim" d="M76 548 L160 548 L300 556 L1052 556 L1078 560 L1078 604 L1052 606 L1052 600 L74 600 Z"/>

  <g class="wheel front-wheel">
    <circle class="wheel-arch" cx="223" cy="600" r="66"/>
    <circle class="tyre" cx="223" cy="601" r="56"/>
    <circle class="rim" cx="223" cy="601" r="34"/>
    <circle class="hub" cx="223" cy="601" r="10"/>
  </g>
  <g class="wheel rear-wheel">
    <circle class="wheel-arch" cx="851" cy="600" r="66"/>
    <circle class="tyre" cx="851" cy="601" r="56"/>
    <circle class="rim" cx="851" cy="601" r="34"/>
    <circle class="hub" cx="851" cy="601" r="10"/>
  </g>
</svg>
</body>
</html>
```